Landscape Supplier and Excavation company needing a website revamp.

We need a web design for our company based out of northern Virginia. We make and deliver topsoil, mulch, and compost. We are also an excavation company. We provide a wide variety of excavation services, from residential to large commercial projects. We specialize in land clearing and building site preparation. We would like a site that looks very professional and makes us look like a large company. We've been in business since 1994 and have never had a really nice website. Our current website it www.hollowbrookloam.com and www.rkqmo.com for references. I like the information on the pages but would like something more professional looking. Doesn't HAVE to be 4 different pages, but I would like a contact form, our services, and our products/ pricing listed. We are properly licensed and insured and would like this included somewhere on the site.

Target Market(s)

Landscapers, Home Owners, Commercial

Industry/Entity Type

Excavation and Landscape Products Supplier

Number of Pages Required

4 page

Colors

Designer to choose colors to be used in the design.

Requirements
Must have
• Professional Look and Feel

```html
<!DOCTYPE html>
<html lang="en">
<head>
<meta charset="utf-8">
<title>Hollowbrook Loam and Excavation</title>
<link href="https://fonts.googleapis.com/css2?family=Poppins:wght@400;600;700&family=Roboto+Slab:wght@700&display=swap" rel="stylesheet">
<style>
:root{
  --red:#c4242a;
  --red-dark:#8e1519;
  --ink:#222;
  --soil:#7a6248;
  --soil-dark:#4d3b2a;
  --fog:#eceef2;
  --night:#2a3224;
  --black:#000;
}
*{box-sizing:border-box;margin:0;padding:0}
html,body{width:1200px;height:2497px;overflow:hidden}
body{font-family:"Poppins",sans-serif;color:var(--ink);background:#fff;position:relative}
.header{position:absolute;top:0;left:0;width:1200px;height:113px}
.brand{position:absolute;left:31px;top:19px;width:337px;height:74px;border:2px solid #222;display:flex;flex-direction:column;align-items:center;justify-content:center}
.brand-name{font-family:"Poppins",sans-serif;font-weight:700;color:var(--red);font-size:26px;line-height:1.1}
.brand-sub{font-weight:600;font-size:14px;letter-spacing:1px;color:#222}
.phone{position:absolute;right:30px;top:10px;display:flex;align-items:center;gap:8px;color:var(--red);font-weight:700;font-size:34px}
.nav{position:absolute;right:0;top:60px;width:720px;height:53px;background:var(--red);border-top-left-radius:50px 53px;display:flex;justify-content:flex-end;align-items:center;gap:50px;padding-right:30px}
.nav a{color:#fff;text-decoration:none;font-size:19px}
.hero{position:absolute;top:113px;left:0;width:1200px;height:514px;background:linear-gradient(180deg,#8a8264 0%,#7d6a50 40%,#6a5440 100%);display:flex;flex-direction:column;align-items:center;padding-top:142px}
.hero h1{color:#fff;font-weight:600;font-size:33px;line-height:52px;text-align:center;text-shadow:0 2px 4px rgba(0,0,0,.7)}
.btn{display:block;width:259px;height:40px;background:var(--red);border-bottom:3px solid var(--red-dark);border-radius:3px;color:#fff;font-size:25px;text-align:center;line-height:38px;text-decoration:none}
.hero .btn{margin-top:12px}
.products{position:absolute;top:694px;left:189px;display:flex;gap:51px}
.tile{width:240px;height:240px;border:2px solid var(--red);padding:7px}
.tile-img{width:100%;height:100%;display:flex;align-items:center;justify-content:center;color:#fff;font-weight:700;font-size:33px;text-shadow:0 2px 4px rgba(0,0,0,.8)}
.products-more{position:absolute;top:969px;left:470px}
.about{position:absolute;top:1079px;left:0;width:1200px;height:428px;background:var(--fog)}
.about-frame{position:absolute;left:47px;top:43px;width:544px;height:342px;border:2px solid var(--red);padding:7px}
.about-img{width:100%;height:100%;background:linear-gradient(160deg,#6d5440,#8d6e54 50%,#3e3a2c)}
.about h2{position:absolute;left:615px;top:36px;color:var(--red);font-size:34px;font-weight:700}
.about p{position:absolute;left:618px;top:95px;width:550px;font-size:17px;line-height:26px;color:#333}
.about .btn{position:absolute;left:619px;top:234px}
.work h2{position:absolute;top:1542px;left:0;width:1254px;text-align:center;color:var(--red);font-size:34px;font-weight:700}
.services{position:absolute;top:1622px;left:30px;display:flex;gap:16px}
.service{width:272px;height:343px;border:2px solid var(--red);padding:7px}
.service-img{position:relative;width:100%;height:100%}
.service-label{position:absolute;bottom:0;left:0;right:0;height:40px;background:rgba(0,0,0,.45);color:#fff;font-size:21px;text-align:center;line-height:42px}
.work-more{position:absolute;top:2010px;left:470px}
.contact{position:absolute;top:2094px;left:0;width:1200px;height:302px;background:linear-gradient(180deg,#3b4334,#2c3326 60%,#252b20)}
.field{position:absolute;border:1px solid #ccc;color:#fff;font-size:17px;padding:6px 18px;background:rgba(0,0,0,.15)}
.contact .btn{position:absolute;left:471px;top:203px}
.footer{position:absolute;top:2396px;left:0;width:1200px;height:101px;background:var(--black);color:#fff}
.footer-nav{display:flex;justify-content:center;gap:50px;padding-top:19px;font-size:19px}
.footer-nav a{color:#fff;text-decoration:none}
.copy{text-align:center;font-size:15px;margin-top:18px}
</style>
</head>
<body>
<header class="header">
  <div class="brand"><span class="brand-name">HOLLOWBROOK</span><span class="brand-sub">LOAM AND EXCAVATION INC.</span></div>
  <div class="phone">
    <svg width="32" height="32" viewBox="0 0 32 32"><circle cx="16" cy="16" r="16" fill="#c4242a"/><path d="M11 8l3 0 1.5 4-2 1.5c1 2.2 2.6 3.8 4.8 4.8l1.5-2 4 1.5v3c0 1-1 2-2 2C14 22.5 9.5 18 9 10c0-1 1-2 2-2z" fill="#fff"/></svg>
    555-018-2744
  </div>
  <nav class="nav"><a href="#">ABOUT US</a><a href="#">SERVICES</a><a href="#">PRODUCTS/PRICING</a><a href="#">CONTACT US</a></nav>
</header>

<section class="hero" role="img" aria-label="Wheel loader working beside large piles of screened topsoil">
  <h1>NOW UNTIL FURTHUR NOTICE<br>WE WILL ONLY BE DOING DELIVERIES,<br>NO RETAIL PICK UP</h1>
  <a class="btn" href="#">CALL NOW</a>
</section>

<section class="products">
  <div class="tile"><div class="tile-img" role="img" aria-label="Topsoil screener at work" style="background:linear-gradient(160deg,#a9b8c6,#7b5c43 55%,#5a4634)">TOPSOIL</div></div>
  <div class="tile"><div class="tile-img" role="img" aria-label="Mulch with shovel beside a red fence" style="background:linear-gradient(180deg,#a4443a,#6b3a2a 60%,#4e9a36)">MULCH</div></div>
  <div class="tile"><div class="tile-img" role="img" aria-label="Hands holding dark compost" style="background:linear-gradient(180deg,#2a211b,#4a3a30 50%,#231a15)">COMPOST</div></div>
</section>
<a class="btn products-more" href="#">LEARN MORE</a>

<section class="about">
  <div class="about-frame"><div class="about-img" role="img" aria-label="Conveyor stacking screened soil"></div></div>
  <h2>ABOUT US</h2>
  <p>Hollowbrook Loam has been providing quality topsoil and mulch since 1992. We strive to produce the very best quality topsoil and lawn amendments for your specific needs. Contact us today to learn more about what we offer and what we can do for you.</p>
  <a class="btn" href="#">LEARN MORE</a>
</section>

<section class="work">
  <h2>WHAT WE DO</h2>
  <div class="services">
    <div class="service"><div class="service-img" role="img" aria-label="Excavator digging" style="background:linear-gradient(180deg,#9fc0e0,#c79a3a 50%,#5b4a36)"><span class="service-label">EXCAVATION</span></div></div>
    <div class="service"><div class="service-img" role="img" aria-label="Conveyor building a topsoil pile" style="background:linear-gradient(180deg,#b7cde2,#5f4a38 40%,#3e3024)"><span class="service-label">TOPSOIL</span></div></div>
    <div class="service"><div class="service-img" role="img" aria-label="Machines clearing wooded land" style="background:linear-gradient(180deg,#3e5a2e,#6b5a45 50%,#7a5238)"><span class="service-label">CLEARING</span></div></div>
    <div class="service"><div class="service-img" role="img" aria-label="Dozer grading a building site" style="background:linear-gradient(180deg,#c9d3dd,#b0b3a8 40%,#a04a30)"><span class="service-label">GRADING</span></div></div>
  </div>
</section>
<a class="btn work-more" href="#">LEARN MORE</a>

<section class="contact" role="img" aria-label="Heavy equipment at a clearing site at dusk">
  <div class="field" style="left:210px;top:60px;width:381px;height:36px">NAME</div>
  <div class="field" style="left:609px;top:62px;width:381px;height:36px">EMAIL</div>
  <div class="field" style="left:210px;top:116px;width:780px;height:73px">MESSAGE</div>
  <a class="btn" href="#">SEND</a>
</section>

<footer class="footer">
  <nav class="footer-nav"><a href="#">ABOUT US</a><a href="#">SERVICES</a><a href="#">PRODUCTS/PRICING</a><a href="#">CONTACT US</a></nav>
  <p class="copy">Copyright © 2020-2021 Hollowbrook Loam - All rights Reserves.</p>
</footer>
</body>
</html>
```